Teskar Business Cards

We need new Business Cards for our startup. It just launched.It is working in the high-end it-market. Specifically in the cloud area. We are a hybrid cloud company. The company logo is attached. We are a Swiss based company. Information visible on the card is: 1. Logo 2. Company Name: Teskar AG 3. Subtitle: Hybrid Clouds. 3. Name: Lukas Brenner 4. Adress: Holderweg 12a, 8462 Talmatt, Switzerland 5. Email: lukas@teskar.example. 6. Mobile: +41 79 304 62 18. It should be a grey/white design. Similar to the attached logo. It should have class, high-quality but not too much color and no gold used.

I forgot to add my Position. Please use Founder / CEO. thanks lukas

```html
<!DOCTYPE html>
<html lang="en">
<head>
<meta charset="utf-8">
<title>Teskar AG – Business Card</title>
<link rel="stylesheet" href="https://fonts.googleapis.com/css2?family=Open+Sans:wght@400;600&display=swap">
<style>
  :root {
    --page-bg: #e6e4e1;
    --card-white: #f7f6f3;
    --band-grey: #58585a;
    --ink-dark: #1e1e1e;
    --ink-grey: #6f6f72;
    --ink-light: #e8e8e8;
    --line-grey: #b9b9bb;
    --plate-light: #f2f2f2;
    --plate-mid: #c9c9cb;
  }
  * { margin: 0; padding: 0; box-sizing: border-box; }
  html, body {
    width: 900px; height: 1200px; overflow: hidden;
    background: var(--page-bg);
    font-family: "Open Sans", Arial, sans-serif;
  }
  .sheet {
    width: 900px; height: 1200px;
    display: flex; flex-direction: column; align-items: center; justify-content: center;
    gap: 90px;
  }
  .card {
    position: relative;
    width: 700px; height: 424px;
    background: var(--card-white);
    box-shadow: 0 6px 18px rgba(0,0,0,0.18);
    overflow: hidden;
  }

  /* Front side */
  .brand {
    position: absolute; left: 70px; top: 120px; width: 300px;
    text-align: center; color: var(--ink-grey);
  }
  .brand-name {
    display: flex; align-items: center; justify-content: center; gap: 14px;
    font-size: 44px; font-weight: 400; letter-spacing: 10px;
  }
  .brand-dot { width: 14px; height: 14px; border-radius: 50%; background: var(--ink-grey); flex: none; }
  .brand-sub { font-size: 17px; letter-spacing: 2px; margin-top: 2px; }

  .name-plate {
    position: absolute; left: 395px; top: 70px; width: 305px; height: 82px;
    background: linear-gradient(100deg, var(--plate-light) 0%, var(--plate-mid) 55%, var(--plate-light) 100%);
    padding: 14px 0 0 24px; color: var(--ink-dark);
  }
  .person-name { font-size: 23px; font-weight: 400; letter-spacing: 1px; line-height: 1.2; }
  .person-role { font-size: 17px; letter-spacing: 0.5px; }

  .contact-band {
    position: absolute; left: 0; top: 258px; width: 700px; height: 108px;
    background: var(--band-grey); color: var(--ink-light);
    font-size: 15px; letter-spacing: 1px; text-transform: uppercase;
  }
  .contact-row { position: absolute; display: flex; align-items: center; gap: 8px; white-space: nowrap; }
  .row-email { right: 40px; top: 14px; }
  .row-phone { left: 128px; top: 46px; }
  .row-address { left: 128px; top: 74px; }
  .icon { width: 16px; height: 16px; fill: var(--ink-light); flex: none; }

  .edge-line {
    position: absolute; left: 0; bottom: 22px; width: 700px; height: 3px;
    background: var(--line-grey);
  }

  /* Back side */
  .brand-back {
    position: absolute; left: 0; top: 150px; width: 700px;
    text-align: center; color: var(--ink-grey);
  }
  .brand-back .brand-name { font-size: 50px; letter-spacing: 12px; }
  .brand-back .brand-sub { font-size: 20px; }

  .site-rule {
    position: absolute; left: 40px; right: 40px; bottom: 40px;
    display: flex; align-items: center; gap: 16px;
  }
  .site-rule .rule { flex: 1; height: 3px; background: var(--line-grey); }
  .site-url { font-size: 15px; font-weight: 600; letter-spacing: 1px; color: var(--ink-dark); text-transform: uppercase; white-space: nowrap; }
</style>
</head>
<body>
<main class="sheet">

  <section class="card card-front">
    <div class="brand">
      <div class="brand-name"><span class="brand-dot"></span>TESKAR</div>
      <div class="brand-sub">HYBRID CLOUDS</div>
    </div>

    <div class="name-plate">
      <div class="person-name">LUKAS BRENNER</div>
      <div class="person-role">Founder / CEO</div>
    </div>

    <div class="contact-band">
      <div class="contact-row row-email">
        <svg class="icon" viewBox="0 0 16 16" aria-hidden="true"><path d="M1 3h14v10H1z M2 4l6 5 6-5" fill="none" stroke="#e8e8e8" stroke-width="1.4"/></svg>
        <span>lukas@teskar.example</span>
      </div>
      <div class="contact-row row-phone">
        <svg class="icon" viewBox="0 0 16 16" aria-hidden="true"><rect x="4" y="1" width="8" height="14" rx="1.5" fill="none" stroke="#e8e8e8" stroke-width="1.4"/><circle cx="8" cy="12.5" r="0.9"/></svg>
        <span>+41 79 304 62 18</span>
      </div>
      <div class="contact-row row-address">
        <svg class="icon" viewBox="0 0 16 16" aria-hidden="true"><path d="M8 1a5 5 0 0 0-5 5c0 4 5 9 5 9s5-5 5-9a5 5 0 0 0-5-5zm0 7a2 2 0 1 1 0-4 2 2 0 0 1 0 4z"/></svg>
        <span>Holderweg 12a, 8462 Talmatt, Switzerland</span>
      </div>
    </div>

    <div class="edge-line"></div>
  </section>

  <section class="card card-back">
    <div class="brand-back">
      <div class="brand-name"><span class="brand-dot"></span>TESKAR</div>
      <div class="brand-sub">HYBRID CLOUDS</div>
    </div>
    <div class="site-rule">
      <span class="rule"></span>
      <span class="site-url">www.teskar.example</span>
      <span class="rule"></span>
    </div>
  </section>

</main>
</body>
</html>
```